Business card for a new innovative and professional lawn care business

We need a business card design for a new lawn care business in Halifax NS Canada. We offer lawn services in Halifax & Bedford. Our services offered include lawn care, garden services, and property maintenance. We take pride in our work and are experienced at what we do. I would like to see a design that is double sided. On the backside I would like the something simple (maybe my logo preferably on blackround (linked below) with website link, Facebook page or something). The front I want to include contact info:
Darren Maple
phone 902-555-0148
email - darrensyardworks.ca
facebook - Facebook.com/darrensyardworks
Instagram maybe ? - instagram.com/darrenyardworks
Serving Halifax and Bedford for 5 years?
I don't want it to have too much information as I will be passing them out in aim to visit website, or call !
We do want it to include lawn care, garden services and property maintenance.
Basic, catchy, and modern looking !
Logo attached below !

Target Market(s)

Passing business cards to everyone I meet or interact with.

Industry/Entity Type

Lawn Care

Contact Information for Business Card

Double sided with some basic information, with catchy colours and easy to look at.

Font styles to use
Sans Serif

Requirements
Must have
• Must be double sided and have :
• Name, Phone, Email, FB, Website, and 3 main services offered - lawn care, property maintenance, garden services
Nice to have
• Would be nice to have instagram link if it goes well on there
Should not have
• Don't want too much writing or images that are distracting

```html
<!DOCTYPE html>
<html lang="en">
<head>
<meta charset="utf-8">
<title>Darren's Yardworks – Business Card</title>
<link href="https://fonts.googleapis.com/css2?family=Open+Sans:wght@400;600;800&display=swap" rel="stylesheet">
<style>
  :root {
    --backdrop: #e9e6df;
    --card-black: #0f1010;
    --card-charcoal: #1d1f1f;
    --leaf-green: #1f9a4e;
    --leaf-deep: #157a3b;
    --lime: #c5e87a;
    --lime-bright: #a6d84a;
    --ink: #3a3d3a;
    --ellipse: #262828;
  }
  html, body {
    margin: 0;
    width: 1200px;
    height: 1023px;
    overflow: hidden;
    background: var(--backdrop);
    font-family: "Open Sans", sans-serif;
  }
  .card {
    position: absolute;
    left: 250px;
    width: 700px;
    height: 400px;
    border-radius: 6px;
    overflow: hidden;
    background: var(--card-black);
    box-shadow: 0 10px 30px rgba(0,0,0,0.25);
  }
  .card--front { top: 60px; }
  .card--back { top: 560px; }
  .card svg.card__art { position: absolute; inset: 0; }

  .brand {
    position: absolute;
    display: flex;
    align-items: center;
    gap: 12px;
    font-weight: 800;
    color: var(--lime-bright);
    letter-spacing: 1px;
    text-transform: uppercase;
    white-space: nowrap;
  }
  .brand__dot {
    width: 18px; height: 18px; border-radius: 50%;
    background: var(--leaf-green);
    flex: none;
  }
  .card--front .brand { top: 44px; left: 150px; font-size: 28px; line-height: 1.2; }
  .card--front .brand__dot { width: 15px; height: 15px; }

  .holder { position: absolute; left: 40px; top: 180px; text-align: right; width: 230px; }
  .holder__name { font-size: 26px; font-weight: 400; color: var(--leaf-green); text-transform: uppercase; margin: 0; }
  .holder__role { font-size: 14px; color: var(--lime-bright); margin: 2px 0 0; }

  .contact { position: absolute; list-style: none; margin: 0; padding: 0; color: var(--ink); font-size: 15px; }
  .contact li { display: flex; align-items: center; gap: 9px; height: 24px; }
  .contact--direct { left: 300px; top: 310px; }
  .contact--social { left: 480px; top: 200px; }
  .icon { width: 15px; height: 15px; border-radius: 3px; background: var(--ink); display: inline-flex; align-items: center; justify-content: center; }
  .icon svg { width: 11px; height: 11px; }
  .icon--plain { background: var(--leaf-deep); }

  .card--back .brand { left: 0; right: 0; top: 165px; justify-content: center; font-size: 40px; }
  .services {
    position: absolute; left: 0; right: 0; bottom: 40px; margin: 0;
    text-align: center; color: var(--lime-bright);
    font-size: 14px; letter-spacing: 1px; text-transform: uppercase;
  }
  .services__sep { color: var(--leaf-green); margin: 0 8px; }
</style>
</head>
<body>

<section class="card card--front">
  <svg class="card__art" viewBox="0 0 700 400" aria-hidden="true">
    <path d="M0,322 C250,285 500,160 700,10 L700,42 C500,185 250,305 0,345 Z" fill="var(--leaf-green)"/>
    <path d="M0,345 C250,305 500,185 700,42 L700,400 L0,400 Z" fill="var(--lime)"/>
  </svg>

  <div class="brand"><span class="brand__dot"></span>Darren's Yardworks</div>

  <div class="holder">
    <p class="holder__name">Darren Maple</p>
    <p class="holder__role">Director</p>
  </div>

  <ul class="contact contact--social">
    <li><span class="icon icon--plain"></span>/darrensyardworks</li>
    <li><span class="icon icon--plain"></span>/darrenyardworks</li>
  </ul>

  <ul class="contact contact--direct">
    <li><span class="icon"><svg viewBox="0 0 12 12"><path d="M2.5 1l2 2.2-1 1.3a6 6 0 0 0 4 4l1.3-1 2.2 2-1.2 1.5C5 11 1 7 1 2.2z" fill="#fff"/></svg></span>902-555-0148</li>
    <li><span class="icon"><svg viewBox="0 0 12 12"><rect x="1" y="2.5" width="10" height="7" fill="none" stroke="#fff" stroke-width="1.2"/><path d="M1 2.5l5 4 5-4" fill="none" stroke="#fff" stroke-width="1.2"/></svg></span>darren@darrensyardworks.ca</li>
    <li><span class="icon"><svg viewBox="0 0 12 12"><circle cx="6" cy="6" r="4.6" fill="none" stroke="#fff" stroke-width="1.2"/><path d="M1.4 6h9.2M6 1.4v9.2" stroke="#fff" stroke-width="1"/></svg></span>www.darrensyardworks.ca</li>
  </ul>
</section>

<section class="card card--back">
  <svg class="card__art" viewBox="0 0 700 400" aria-hidden="true">
    <ellipse cx="350" cy="190" rx="290" ry="175" fill="var(--ellipse)"/>
    <ellipse cx="350" cy="190" rx="240" ry="140" fill="var(--card-charcoal)"/>
  </svg>

  <div class="brand"><span class="brand__dot"></span>Darren's Yardworks</div>

  <p class="services">Lawn Care<span class="services__sep">●</span>Property Maintenance<span class="services__sep">●</span>Garden Services</p>
</section>

</body>
</html>
```